Business Card Design for Varnok Facility Services

We are looking for a Business Card Design for the Company "Varnok Facility Services."
Front side:
- Company Logo (small)
- Company Name, address, pohone, website and personal data.
- white background, for text e.g. company colors (blue or green like in the logo)
Please use following data:
Company data:
Varnok Facility Services Tulbrecht
Kirchmattweg 12
6331 Cham
www.varnok-fs.ch
Person data:
Ruben Tulbrecht
Geschäftsführer
+41 76 519 84 60
info@varnok-fs.ch
Back side:
could be colored in blue or green
please use a big logo sing and some smaller icons to say what is all beeing offered in facility services, like cleaning, maintenance cleaning
industrial cleaning, caretaking, gardening, disposal. There is no need for everyone of the icons if there are similar or an icon is standing for more of them.
Cleaning Service
colors to use:
blue: HEX 246BB0
green: HEX 52B33E

```html
<!DOCTYPE html>
<html lang="de">
<head>
<meta charset="utf-8">
<title>Varnok Facility Services – Visitenkarte</title>
<link rel="stylesheet" href="https://fonts.googleapis.com/css2?family=Montserrat:wght@400;500;600&display=swap">
<style>
  :root {
    --backdrop: #161616;
    --card: #262626;
    --card-edge: #303030;
    --map-light: #2f2f2f;
    --map-dark: #232323;
    --brand-blue: #246BB0;
    --brand-green: #52B33E;
    --text-light: #f2f2f2;
  }
  * { box-sizing: border-box; margin: 0; padding: 0; }
  html, body {
    width: 1200px; height: 900px; overflow: hidden;
    background: var(--backdrop);
    font-family: "Montserrat", sans-serif;
  }
  .canvas { position: relative; width: 1200px; height: 900px; }
  .card {
    position: absolute; left: 250px; width: 700px; height: 400px;
    background: var(--card);
    border: 1px solid var(--card-edge);
    overflow: hidden;
  }
  .card--back { top: 35px; }
  .card--front { top: 465px; }
  .map-texture {
    position: absolute; inset: 0;
    background: linear-gradient(135deg, var(--map-light) 0%, var(--map-dark) 100%);
  }
  .brand {
    position: absolute; display: flex; align-items: center; gap: 18px;
    color: var(--brand-blue); font-weight: 600;
  }
  .brand-dot {
    width: 52px; height: 52px; border-radius: 50%;
    background: var(--brand-green); flex: none;
  }
  .brand-name { line-height: 1.05; }
  .brand-name .primary { display: block; font-size: 56px; letter-spacing: 5px; text-transform: uppercase; }
  .brand-name .secondary { display: block; font-size: 18px; letter-spacing: 5.5px; text-transform: uppercase; margin-top: 4px; }
  .card--back .brand { left: 50%; top: 50%; transform: translate(-50%, -50%); }
  .card--front .brand {
    left: 40px; top: 112px; width: 300px;
    flex-direction: column; gap: 14px;
  }
  .card--front .brand-name { text-align: center; }
  .card--front .brand-name .primary { font-size: 46px; letter-spacing: 4px; }
  .card--front .brand-name .secondary { font-size: 15px; letter-spacing: 4px; }
  .divider {
    position: absolute; left: 370px; top: 100px; width: 2px; height: 205px;
    background: var(--brand-blue);
  }
  .contact {
    position: absolute; left: 398px; top: 98px; color: var(--text-light);
    font-size: 17px; line-height: 1.3;
  }
  .contact .person { color: var(--brand-blue); font-weight: 600; font-size: 24px; line-height: 1.2; }
  .contact .role { margin-bottom: 8px; }
  .contact .address { margin-bottom: 8px; font-size: 18px; }
  .contact-line { display: flex; align-items: center; gap: 9px; }
  .contact-line svg { width: 14px; height: 14px; flex: none; }
  .contact .web strong { font-weight: 600; }
</style>
</head>
<body>
<main class="canvas">
  <section class="card card--back">
    <div class="map-texture" role="img" aria-label="Faint world map in the background"></div>
    <div class="brand">
      <span class="brand-dot"></span>
      <span class="brand-name"><span class="primary">Varnok</span><span class="secondary">Facility Services</span></span>
    </div>
  </section>

  <section class="card card--front">
    <div class="map-texture" role="img" aria-label="Faint world map in the background"></div>
    <div class="brand">
      <span class="brand-dot"></span>
      <span class="brand-name"><span class="primary">Varnok</span><span class="secondary">Facility Services</span></span>
    </div>
    <div class="divider"></div>
    <div class="contact">
      <p class="person">Ruben Tulbrecht</p>
      <p class="role">Geschäftsführer</p>
      <p class="address">Kirchmattweg 12<br>6331 Cham</p>
      <p class="contact-line">
        <svg viewBox="0 0 16 16"><path d="M4 1l3 3-2 2c1 2 3 4 5 5l2-2 3 3-2 3C7 15 1 9 1 3z" fill="var(--brand-blue)"/></svg>
        +41 76 519 84 60
      </p>
      <p class="contact-line">
        <svg viewBox="0 0 16 16"><rect x="1" y="3" width="14" height="10" fill="none" stroke="var(--brand-blue)" stroke-width="1.5"/><path d="M1 3l7 6 7-6" fill="none" stroke="var(--brand-blue)" stroke-width="1.5"/></svg>
        info@varnok-fs.ch
      </p>
      <p class="contact-line web">
        <svg viewBox="0 0 16 16"><circle cx="8" cy="8" r="6.5" fill="none" stroke="var(--brand-blue)" stroke-width="1.5"/><ellipse cx="8" cy="8" rx="3" ry="6.5" fill="none" stroke="var(--brand-blue)" stroke-width="1.2"/><path d="M1.5 8h13" stroke="var(--brand-blue)" stroke-width="1.2"/></svg>
        <span>www.<strong>varnok-fs</strong>.ch</span>
      </p>
    </div>
  </section>
</main>
</body>
</html>
```